Kerris Odlen Letter Head

log and letter head

would like a modern feminine approch, please see attached the back of my business card

Kerris Odlen Consulting

ABN 81 540 263 918

Address19a Brood Street Marlow Heights 5082 Calder Vale

Business

```html
<!DOCTYPE html>
<html lang="en">
<head>
<meta charset="utf-8">
<title>Kerris Odlen Consulting – Letterhead</title>
<link rel="stylesheet" href="https://fonts.googleapis.com/css2?family=Noticia+Text:wght@400;700&family=Montserrat:wght@400;600&display=swap">
<style>
  :root {
    --brand-red: #ec1c24;
    --brand-red-deep: #d3191f;
    --paper: #ffffff;
    --ink: #3a3a3a;
    --backdrop: #e6e6e6;
    --on-red: #ffffff;
  }
  * { margin: 0; padding: 0; box-sizing: border-box; }
  html, body {
    width: 1200px; height: 900px; overflow: hidden;
    background: var(--backdrop);
    font-family: "Noticia Text", Georgia, serif;
  }
  .canvas { position: relative; width: 1200px; height: 900px; }

  .sheet { position: absolute; top: 93px; width: 504px; height: 710px; }
  .sheet--front { left: 81px; background: var(--paper); }
  .sheet--back { left: 615px; background: var(--brand-red); }

  .header-band {
    position: absolute; left: 0; top: 0; width: 100%; height: 62px;
    background: var(--brand-red);
  }
  .back-fill { position: absolute; inset: 0; background: var(--brand-red); }

  .wordmark {
    position: absolute; left: 0; width: 100%; text-align: center;
    color: var(--on-red); font-weight: 400;
  }
  .wordmark__name { display: block; }
  .wordmark__line {
    display: block; text-transform: uppercase;
    font-family: "Montserrat", Arial, sans-serif; font-weight: 400;
  }

  .wordmark--header { top: 14px; }
  .wordmark--header .wordmark__name { font-size: 22px; line-height: 26px; }
  .wordmark--header .wordmark__line { font-size: 6.5px; letter-spacing: 4.2px; margin-top: 3px; padding-left: 4px; }

  .wordmark--cover { top: 312px; }
  .wordmark--cover .wordmark__name { font-size: 44px; line-height: 52px; }
  .wordmark--cover .wordmark__line { font-size: 10px; letter-spacing: 9px; margin-top: 6px; padding-left: 9px; }

  .letter-meta {
    position: absolute; left: 52px; top: 169px;
    font-size: 8.8px; font-weight: 700; line-height: 14.5px; color: var(--ink);
  }
  .letter-body {
    position: absolute; left: 52px; top: 231px; width: 399px;
    font-size: 8.8px; line-height: 14.5px; color: var(--ink);
  }
  .letter-body p { margin-bottom: 14.5px; }
  .letter-body .line {
    display: block; text-align: justify; text-align-last: justify; white-space: nowrap;
  }
  .letter-body .line--end { text-align-last: left; }
  .letter-body .signoff { margin-top: 14.5px; }

  .footer-band {
    position: absolute; left: 0; bottom: 0; width: 100%; height: 24px;
    background: var(--brand-red-deep); color: var(--on-red);
    font-family: "Montserrat", Arial, sans-serif;
    font-size: 6.2px; font-weight: 600;
    display: flex; align-items: center; justify-content: space-between;
    padding: 0 26px 0 21px;
  }
  .footer-band__address { display: flex; align-items: center; gap: 4px; }
  .footer-band__address svg { width: 10px; height: 10px; }
</style>
</head>
<body>
<main class="canvas">

  <section class="sheet sheet--front" aria-label="Letterhead">
    <div class="header-band" role="img" aria-label="Red header band with a faint floral scroll pattern"></div>
    <div class="wordmark wordmark--header">
      <span class="wordmark__name">Kerris Odlen</span>
      <span class="wordmark__line">Consulting</span>
    </div>

    <div class="letter-meta">
      <div>TO: Elena Marsh</div>
      <div>Subject: Order status</div>
      <div>Date: 30.01.2012</div>
    </div>

    <div class="letter-body">
      <span class="line line--end">Dear Ms. Elena Marsh,</span>
      <p>
        <span class="line">Ut malesuada velit et augue fringilla sed elementum ipsum facilisis. Sed nec eros et neque posuere</span>
        <span class="line">dictum. Pellentesque a massa mi. Quisque nec neque risus, non suscipit magna. Aenean pulvinar</span>
        <span class="line">pellentesque rutrum. Integer interdum, justo vel malesuada bibendum, mi elit feugiat est, vel</span>
        <span class="line line--end">mattis tellus massa faucibus diam. Nulla sed elit est, ut condimentum odio.</span>
      </p>
      <p>
        <span class="line">Nunc venenatis massa sit amet turpis luctus vel tempus felis malesuada. Curabitur volutpat</span>
        <span class="line">sodales tincidunt. Donec consectetur ultricies dolor, vel malesuada nibh consectetur vitae.</span>
        <span class="line line--end">Pellentesque semper urna non lorem venenatis non consequat dolor commodo.</span>
      </p>
      <p>
        <span class="line">Donec ac lorem erat, in euismod eros. Cras non suscipit ligula. Nam sodales, arcu vel ornare</span>
        <span class="line">ullamcorper, sapien turpis eleifend est, nec porttitor turpis neque imperdiet odio. Aenean quam</span>
        <span class="line">mi, sodales vel tincidunt non, gravida vitae nunc. Phasellus eu felis nisi. Ut ut nibh ipsum, rhoncus</span>
        <span class="line line--end">luctus lacus.</span>
      </p>
      <p>
        <span class="line">In hac habitasse platea dictumst. Suspendisse potenti. Donec nec erat ac dolor imperdiet</span>
        <span class="line">scelerisque non eget quam. Aenean velit augue, condimentum eu feugiat eget, venenatis eu erat.</span>
        <span class="line">Ut fermentum bibendum libero et imperdiet. Vivamus at lorem vel quam feugiat tempus ut sed</span>
        <span class="line line--end">nulla. Vivamus adipiscing tellus non erat vulputate rhoncus sed a risus.</span>
      </p>
      <span class="line line--end signoff">Best regards,</span>
    </div>

    <footer class="footer-band">
      <span class="footer-band__address">
        <svg viewBox="0 0 10 10" aria-hidden="true">
          <circle cx="5" cy="5" r="5" fill="#ffffff"/>
          <path d="M5 2.2a1.9 1.9 0 0 0-1.9 1.9C3.1 5.5 5 7.8 5 7.8s1.9-2.3 1.9-3.7A1.9 1.9 0 0 0 5 2.2z" fill="#d3191f"/>
          <circle cx="5" cy="4.1" r="0.7" fill="#ffffff"/>
        </svg>
        27c Tallow Lane Marlow Heights 5082 Calder Vale
      </span>
      <span class="footer-band__abn">ABN 81 540 263 918</span>
    </footer>
  </section>

  <section class="sheet sheet--back" aria-label="Letterhead reverse">
    <div class="back-fill" role="img" aria-label="Full red field with a faint all-over floral scroll pattern"></div>
    <div class="wordmark wordmark--cover">
      <span class="wordmark__name">Kerris Odlen</span>
      <span class="wordmark__line">Consulting</span>
    </div>
  </section>

</main>
</body>
</html>
```